business card for a massage therapy practice named 'Meadow and Willow Massage Studio'

I really need a trendy, yet easy on the eyes business card to complement my logo. Ideally with some gold or rose gold foil work.

My uploaded file of the logo I have in horizontal but I have a vertical version as well. Another color that is used in the website is a blush pink here and there. I'd like to see some trendy tropical leaves in the design.

```html
<!DOCTYPE html>
<html lang="en">
<head>
<meta charset="utf-8">
<title>Meadow and Willow Massage Studio – Business Card</title>
<link rel="stylesheet" href="https://fonts.googleapis.com/css2?family=Allura&family=Domine:wght@600&display=swap">
<style>
  :root {
    --backdrop: #dcdcda;
    --blush-light: #f8c6bc;
    --blush: #f1b0a4;
    --blush-deep: #e9a396;
    --rose-foil: #c0673f;
    --rose-script: #d98a68;
    --card-white: #ffffff;
    --shadow: rgba(0, 0, 0, 0.28);
  }
  html, body {
    margin: 0;
    padding: 0;
    width: 1200px;
    height: 866px;
    overflow: hidden;
    background: var(--backdrop);
  }
  .canvas {
    position: relative;
    width: 1200px;
    height: 866px;
  }
  .card {
    position: absolute;
    top: 165px;
    width: 308px;
    height: 538px;
    box-shadow: 3px 4px 6px var(--shadow);
  }
  .card-front {
    left: 198px;
    background: linear-gradient(160deg, var(--blush-light) 0%, var(--blush) 55%, var(--blush-deep) 100%);
  }
  .card-back {
    left: 694px;
    height: 543px;
    background: var(--card-white);
  }
  .brand {
    position: absolute;
    left: 0;
    right: 0;
    top: 392px;
    transform: translateY(-50%);
    display: flex;
    align-items: center;
    justify-content: center;
    gap: 10px;
  }
  .brand-dot {
    width: 26px;
    height: 26px;
    border-radius: 50%;
    background: var(--rose-foil);
    flex: none;
  }
  .brand-name {
    font-family: "Domine", Georgia, serif;
    font-weight: 600;
    color: var(--rose-foil);
    font-size: 17px;
    line-height: 1.25;
    letter-spacing: 0.02em;
    margin: 0;
  }
  .holder-name {
    position: absolute;
    right: 26px;
    top: 14px;
    margin: 0;
    font-family: "Allura", cursive;
    font-weight: 400;
    color: var(--rose-script);
    text-align: right;
    line-height: 1;
  }
  .holder-first {
    display: block;
    font-size: 78px;
  }
  .holder-last {
    display: block;
    font-size: 54px;
    margin-top: -10px;
    margin-right: 6px;
  }
  .contact {
    position: absolute;
    left: 16px;
    top: 392px;
    margin: 0;
    font-family: "Domine", Georgia, serif;
    font-weight: 600;
    color: var(--rose-foil);
    font-style: normal;
  }
  .contact-line {
    display: block;
    font-size: 18.5px;
    line-height: 24px;
    text-transform: uppercase;
  }
  .contact-email {
    display: block;
    font-size: 11px;
    line-height: 14px;
    margin-top: 8px;
    text-transform: uppercase;
  }
  .contact-phone {
    display: block;
    font-size: 18px;
    line-height: 22px;
    margin-top: 16px;
  }
</style>
</head>
<body>
<main class="canvas">
  <section class="card card-front" aria-label="Card front">
    <div class="brand">
      <span class="brand-dot" aria-hidden="true"></span>
      <p class="brand-name">Meadow &amp; Willow<br>Massage Studio</p>
    </div>
  </section>

  <section class="card card-back" aria-label="Card back">
    <h1 class="holder-name">
      <span class="holder-first">Marisol</span>
      <span class="holder-last">Vega</span>
    </h1>
    <address class="contact">
      <span class="contact-line">LMT #58203</span>
      <span class="contact-line">2418 Linden Ave. Suite 210</span>
      <span class="contact-line">Fairbrook, CA 90017</span>
      <span class="contact-email">meadowandwillow@example.com</span>
      <span class="contact-phone">Call or Text:&nbsp; (555) 214-0387</span>
    </address>
  </section>
</main>
</body>
</html>
```